A4 Flyer for charity car show

The "Brook Vale Charity Motor Fair" is an annual event that supports a different charity each year. The event aims to aim money and awareness for a cause as well as display a wide range of different cars that are in the community. These include classic cars, muscle cars, exotic cars and many more.

Information to be included:

The event will be held on: 15th of July 2018.
Charity Supported: Proudly supporting Skyward Care Australia
Location: Renwick Oval, Dorrigal
Website: http://www.brookvalemotorfair.com.au/

Target Market(s)

Car enthusiasts, professionals

Industry/Entity Type

Charity

Requirements
Must have
• Any car used in the flyer must look like they are in a field. Cars used must be right hand drive.

```html
<!DOCTYPE html>
<html lang="en">
<head>
<meta charset="utf-8">
<title>Brook Vale Charity Motor Fair – Flyer</title>
<link rel="stylesheet" href="https://fonts.googleapis.com/css2?family=Montserrat:wght@400;500;700;800&family=Dosis:wght@400;500&display=swap">
<style>
  :root {
    --navy: #163f6b;
    --orange: #f28a22;
    --white: #ffffff;
    --page: #e9eaec;
    --grass: #5f8a3a;
    --sky: #c9cfd3;
    --car-red: #c8332a;
    --ink: #1b2a3a;
  }
  * { box-sizing: border-box; margin: 0; padding: 0; }
  html, body { width: 1200px; height: 899px; overflow: hidden; }
  body {
    background: var(--page);
    font-family: "Montserrat", Arial, sans-serif;
    position: relative;
  }
  .flyer {
    position: absolute;
    left: 294px;
    top: 20px;
    width: 612px;
    height: 860px;
    background: var(--white);
    box-shadow: 0 6px 24px rgba(0,0,0,.18);
    overflow: hidden;
  }
  .hero {
    position: absolute;
    left: 0; top: 0;
    width: 612px; height: 349px;
    background:
      linear-gradient(180deg, var(--sky) 0%, #e3ddd2 38%, transparent 48%),
      radial-gradient(ellipse 60% 32% at 55% 62%, var(--car-red) 0%, #a42a22 55%, transparent 72%),
      linear-gradient(180deg, #b9c0c2 0%, #8fa07a 55%, var(--grass) 75%, #4d7430 100%);
  }
  .brand {
    position: absolute;
    left: 24px; top: 26px;
    display: flex; align-items: center; gap: 10px;
  }
  .brand-dot {
    width: 38px; height: 38px; border-radius: 50%;
    background: var(--navy);
  }
  .brand-name {
    color: var(--orange);
    font-weight: 700;
    font-size: 15px;
    line-height: 1.1;
    letter-spacing: .5px;
    text-transform: uppercase;
  }
  .info {
    position: absolute;
    left: 0; top: 353px;
    width: 612px; height: 288px;
    background: var(--navy);
    color: var(--white);
    text-align: center;
  }
  .title-light {
    margin-top: 22px;
    font-weight: 400;
    font-size: 44px;
    letter-spacing: 1px;
    line-height: 1;
  }
  .title-bold {
    margin-top: 6px;
    font-weight: 800;
    font-size: 39px;
    line-height: 1.1;
    letter-spacing: .5px;
  }
  .cause {
    margin-top: 8px;
    font-size: 17.5px;
    font-weight: 500;
  }
  .date {
    display: inline-block;
    margin-top: 16px;
    background: var(--orange);
    border-radius: 32px;
    padding: 6px 26px 4px;
    font-family: "Dosis", "Arial Narrow", sans-serif;
    font-size: 46px;
    font-weight: 400;
    line-height: 1.1;
    letter-spacing: .5px;
  }
  .venue {
    margin-top: 12px;
    font-size: 26px;
    font-weight: 400;
    letter-spacing: .5px;
  }
  .gallery {
    position: absolute;
    left: 0; top: 645px;
    width: 612px; height: 120px;
  }
  .rule {
    position: absolute;
    left: 0; top: 767px;
    width: 612px; height: 3px;
    background: var(--orange);
  }
  .sponsors {
    position: absolute;
    left: 0; top: 770px;
    width: 612px; height: 44px;
    display: flex; align-items: center; justify-content: space-around;
    padding: 0 24px;
  }
  .sponsor-name { font-weight: 700; font-size: 14px; }
  .sponsor-name.red { color: #c4261d; }
  .sponsor-name.dark { color: var(--ink); font-size: 12px; }
  .sponsor-name.blue { color: #2a3f9a; font-size: 11px; }
  .badge { width: 22px; height: 22px; border-radius: 50%; }
  .badge.green { background: #3f7a3a; }
  .badge.sky { background: #7da3c8; }
  .badge.gold { background: #e0b327; border-radius: 4px; }
  .footer {
    position: absolute;
    left: 0; top: 814px;
    width: 612px; height: 46px;
    background: var(--orange);
    color: var(--white);
    text-align: center;
    font-size: 14.5px;
    letter-spacing: 4.2px;
    line-height: 46px;
  }
</style>
</head>
<body>
  <main class="flyer">
    <div class="hero" role="img" aria-label="Photo of a red classic muscle car parked on a grassy field under a cloudy sky"></div>
    <div class="brand">
      <span class="brand-dot"></span>
      <span class="brand-name">Brook Vale<br>Charity Motor Fair</span>
    </div>

    <section class="info">
      <h1 class="title-light">BROOK VALE</h1>
      <h2 class="title-bold">CHARITY MOTOR FAIR</h2>
      <p class="cause">Proudly supporting Skyward Care Australia</p>
      <p class="date">15TH OF JULY 2018</p>
      <p class="venue">Renwick Oval, Dorrigal</p>
    </section>

    <svg class="gallery" viewBox="0 0 612 120" aria-label="Strip of three classic car photos on grass">
      <polygon role="img" aria-label="Photo of a dark green vintage sedan on grass" points="0,0 225,0 155,120 0,120" fill="#4f6e3c"/>
      <polygon role="img" aria-label="Photo of a black classic coupe on grass" points="231,0 460,0 390,120 161,120" fill="#3d4f33"/>
      <polygon role="img" aria-label="Photo of a lime green hot rod on grass" points="466,0 612,0 612,120 396,120" fill="#8da84a"/>
    </svg>

    <div class="rule"></div>
    <div class="sponsors">
      <span class="sponsor-name red">Ember</span>
      <span class="badge green"></span>
      <span class="sponsor-name dark">Kestrel</span>
      <span class="badge sky"></span>
      <span class="badge gold"></span>
      <span class="sponsor-name blue">Dorrigal Rovers</span>
      <span class="sponsor-name dark">Hartley Legal</span>
    </div>
    <footer class="footer">www.brookvalemotorfair.com.au</footer>
  </main>
</body>
</html>
```